Templates for ppt, word and a new, modern and fresh "look" for this...

We need some new templates for our product datasheet, manuals and powerpoint templates. We are a manufacturer and distributor of gas saving equipment for welding industry mainly.

```html
<!DOCTYPE html>
<html lang="en">
<head>
<meta charset="utf-8">
<title>Fluxa – Document and Presentation Templates</title>
<link rel="stylesheet" href="https://fonts.googleapis.com/css2?family=Source+Sans+3:ital,wght@0,300;0,400;0,600;0,700;1,400&display=swap">
<style>
:root{
  --bg:#cbcbcb;
  --navy:#262b6d;
  --red:#d2232a;
  --ice:#d8edf9;
  --row-grey:#e2e2e2;
  --head-grey:#cdcdcd;
  --ink:#2a2a2a;
  --muted:#8a8a8a;
  --rule:#bdbdbd;
  --bubble:#aaa5a5;
  --sub:#a7a7c4;
}
*{margin:0;padding:0;box-sizing:border-box}
html,body{width:1200px;height:1200px;overflow:hidden;background:var(--bg)}
body{font-family:"Source Sans 3",sans-serif;color:var(--ink);position:relative}
.board-title{position:absolute;left:70px;color:#fff;font-weight:600;font-size:27px;letter-spacing:.2px;line-height:1}
.board-title--docs{top:28px}
.board-title--slides{top:481px;left:65px}

/* ---------- one pager sheets ---------- */
.sheet{position:absolute;top:65px;width:276px;height:390px;background:#fff;box-shadow:0 3px 9px rgba(0,0,0,.22);overflow:hidden}
.sheet--brand{left:74px}
.sheet--headline{left:389px}
.sheet--bar{left:704px}
.sheet *{position:absolute}
.brand-name{color:var(--navy);font-weight:700;line-height:1;white-space:nowrap}
.brand-tag{color:var(--navy);font-weight:400;white-space:nowrap;line-height:1}
.sheet-brand{left:18px;top:16px;width:80px;height:30px}
.sheet--bar .sheet-brand{top:11px}
.sheet-brand .brand-name{left:0;top:0;font-size:22px}
.sheet-brand .brand-tag{left:11px;top:21px;font-size:3.6px}
.head-rule{left:101px;top:33px;width:156px;height:.8px;background:var(--red)}
.sheet--bar .head-rule{top:29px}
.head-contact{right:19px;top:27px;font-size:3.2px;color:var(--navy);white-space:nowrap}
.sheet--bar .head-contact{top:23px}
.head-tab{left:24px;top:0;width:8px;height:19px;background:var(--red)}
.head-title{left:24px;top:24px;font-size:11px;font-weight:400;color:var(--navy);letter-spacing:.1px}
.head-line{left:24px;top:38px;width:230px;height:.5px;background:#d5d5d5}

.intro-title{left:18px;top:48px;font-size:7px;font-weight:400}
.sheet--headline .intro-title{left:26px}
.intro-copy{left:18px;top:58px;width:236px;font-size:4.6px;line-height:7.9px}
.sheet--headline .intro-copy{left:26px;width:232px}

.cost-table{left:16px;top:114px;display:grid;grid-template-columns:125px 43px 74px;column-gap:3px;row-gap:3.3px;grid-auto-rows:6.6px;font-size:4.3px}
.sheet--headline .cost-table{left:24px;top:119px;grid-template-columns:123px 43px 65px}
.cost-table > div{position:static;display:flex;align-items:center;justify-content:center;white-space:nowrap}
.cell{background:var(--ice)}
.cell--task{justify-content:flex-start !important;padding-left:6px}
.cell--head{background:var(--head-grey);color:#444}
.cell--phase{grid-column:1/-1;justify-content:flex-start !important;padding-left:6px;color:var(--navy);font-weight:700}
.cell--total{background:var(--row-grey);font-weight:600}
.cell--grand{background:var(--navy);color:#fff;font-weight:600}
.sheet--headline .cell--grand,.sheet--bar .cell--grand{background:var(--row-grey);color:var(--ink)}

.chart-title{left:16px;top:244px;font-size:6.6px;font-weight:600;color:#333}
.sheet--headline .chart-title{left:24px;top:248px}
.chart-copy{left:16px;top:257px;width:84px;font-size:4.3px;line-height:7.8px}
.sheet--headline .chart-copy{left:24px;top:260px;width:92px}
.pie-small{left:155px;top:259px;width:62px;height:66px}
.sheet--headline .pie-small{left:159px;top:262px}
.pie-label{font-size:2.4px;color:#555;white-space:nowrap}
.pie-label--l{right:126px;text-align:right}
.sheet--headline .pie-label--l{right:122px}
.pie-label--r{left:218px}
.sheet--headline .pie-label--r{left:222px}
.legend{left:118px;top:333px;display:grid;grid-template-columns:repeat(4,33px);row-gap:4px;font-size:2.4px;color:#555}
.sheet--headline .legend{left:130px;top:335px}
.legend span{position:static;display:flex;align-items:center;gap:2px;white-space:nowrap}
.legend i{position:static;display:inline-block;width:4px;height:3px}

.foot-line{left:16px;top:369px;width:244px;height:.6px;background:#9a9a9a}
.foot-text{left:0;width:276px;top:373px;text-align:center;font-size:3.2px;color:#444;white-space:nowrap}
.foot-brand{left:24px;top:364px;font-size:10px}
.foot-brand-tag{left:31px;top:373px;font-size:1.8px;color:var(--navy)}
.foot-rule{left:68px;top:374px;width:186px;height:.5px;background:#9a9a9a}
.foot-contact{right:22px;font-size:2.7px;color:#444;white-space:nowrap;text-align:right}
.foot-bar{left:16px;top:371px;width:243px;height:6px;background:var(--navy);color:#fff;font-size:3.2px;font-weight:600;display:flex;align-items:center;justify-content:center;white-space:nowrap}

/* ---------- slides ---------- */
.slide{position:absolute;width:486px;height:274px;background:#fff;box-shadow:0 3px 9px rgba(0,0,0,.22);overflow:hidden}
.slide--cover{left:71px;top:523px}
.slide--contents{left:623px;top:523px}
.slide--content{left:71px;top:841px}
.slide--closing{left:623px;top:841px}
.slide > *{position:absolute}
.slide-shape{left:0;top:0;width:486px;height:274px}
.cover-title{left:37px;top:29px;color:#fff;font-size:20.5px;font-weight:400;line-height:22px;letter-spacing:.3px}
.cover-sub{left:37px;top:94px;color:var(--sub);font-size:12.4px;font-weight:600;line-height:16px;letter-spacing:.2px}
.cover-brand{left:352px;top:210px;font-size:36px}
.cover-tag{left:366px;top:244px;font-size:6.8px}

.contents-title{left:25px;top:19px;font-size:16.5px;font-weight:700;color:#fff;letter-spacing:.2px}
.contents-title span{color:var(--sub)}
.contents-copy{left:25px;top:45px;width:200px;color:#fff;font-size:7.4px;line-height:10.6px}
.step-num{width:44px;height:44px;border-radius:50%;background:var(--bubble);border:3px solid #fff;color:#fff;font-size:15px;font-weight:600;display:flex;align-items:center;justify-content:center}
.step-num--1{left:221px;top:86px}
.step-num--2{left:157px;top:130px}
.step-num--3{left:89px;top:178px}
.step{width:200px}
.step h4{font-size:9.4px;font-weight:600;color:var(--red);line-height:12px}
.step p{font-size:7.3px;color:#555;line-height:12.8px;margin-top:1px}
.step--1{left:276px;top:87px}
.step--2{left:216px;top:138px}
.step--3{left:141px;top:189px}

.slide-brand{left:21px;top:243px;font-size:16px}
.slide-brand-tag{left:28px;top:258px;font-size:2.8px}
.slide-rule{left:79px;top:255px;width:372px;height:1px;background:#a5a5a5}
.page-num{left:452px;top:249px;width:13px;height:13px;border-radius:50%;background:var(--red);color:#fff;font-size:6.5px;display:flex;align-items:center;justify-content:center;box-shadow:0 0 0 1.5px #fff}

.content-title{left:21px;top:20px;font-size:13px;color:var(--navy);font-weight:400}
.content-line{left:21px;top:37px;width:445px;height:.6px;background:#d2d2d2}
.pie-large{left:32px;top:71px;width:112px;height:120px}
.legend--large{left:40px;top:196px;display:grid;grid-template-columns:repeat(4,30px);row-gap:4px;font-size:2.3px;color:#555}
.legend--large span{display:flex;align-items:center;gap:2px;white-space:nowrap}
.legend--large i{display:inline-block;width:3.5px;height:3px}
.content-copy{left:142px;top:58px;font-size:7.55px;line-height:12px;color:#222}
.content-copy span{display:block;white-space:nowrap}
.content-copy .copy-sub{color:var(--navy);font-style:italic;font-size:8px}

.closing-brand{left:159px;top:231px;font-size:16px}
.closing-tag{left:166px;top:247px;font-size:2.8px}
.closing-sep{left:217px;top:234px;width:.6px;height:14px;background:#888}
.closing-info{font-size:3.8px;line-height:5px;color:var(--navy);white-space:nowrap}
.closing-info--a{left:222px;top:234px}
.closing-info--b{left:282px;top:237px}
.visually-hidden{position:absolute;width:0;height:0;overflow:hidden}
</style>
</head>
<body>

<svg class="visually-hidden" aria-hidden="true">
  <defs>
    <symbol id="pie" viewBox="0 0 100 106">
      <ellipse cx="50" cy="56" rx="44" ry="44" fill="#4e4e9e"/>
      <g transform="rotate(-90 50 47)">
        <circle cx="50" cy="47" r="22" fill="none" stroke-width="44" pathLength="100" stroke="#80b9e1" stroke-dasharray="31.1 68.9" stroke-dashoffset="0"/>
        <circle cx="50" cy="47" r="22" fill="none" stroke-width="44" pathLength="100" stroke="#6f97d8" stroke-dasharray="18.7 81.3" stroke-dashoffset="-31.1"/>
        <circle cx="50" cy="47" r="22" fill="none" stroke-width="44" pathLength="100" stroke="#6770c2" stroke-dasharray="12.4 87.6" stroke-dashoffset="-49.8"/>
        <circle cx="50" cy="47" r="22" fill="none" stroke-width="44" pathLength="100" stroke="#7a60b6" stroke-dasharray="10.3 89.7" stroke-dashoffset="-62.2"/>
        <circle cx="50" cy="47" r="22" fill="none" stroke-width="44" pathLength="100" stroke="#9262b7" stroke-dasharray="6.6 93.4" stroke-dashoffset="-72.5"/>
        <circle cx="50" cy="47" r="22" fill="none" stroke-width="44" pathLength="100" stroke="#ad6cbd" stroke-dasharray="8 92" stroke-dashoffset="-79.1"/>
        <circle cx="50" cy="47" r="22" fill="none" stroke-width="44" pathLength="100" stroke="#c676b9" stroke-dasharray="6.1 93.9" stroke-dashoffset="-87.1"/>
        <circle cx="50" cy="47" r="22" fill="none" stroke-width="44" pathLength="100" stroke="#d870a8" stroke-dasharray="3.7 96.3" stroke-dashoffset="-93.2"/>
        <circle cx="50" cy="47" r="22" fill="none" stroke-width="44" pathLength="100" stroke="#d9608a" stroke-dasharray="3.1 96.9" stroke-dashoffset="-96.9"/>
      </g>
    </symbol>
  </defs>
</svg>

<h1 class="board-title board-title--docs">One pager template</h1>

<!-- Sheet 1 -->
<article class="sheet sheet--brand">
  <div class="sheet-brand"><span class="brand-name">Fluxa</span><span class="brand-tag">Gas saving for welding</span></div>
  <div class="head-rule"></div>
  <p class="head-contact">Tel: +46(0)300-555 10 &nbsp;| &nbsp;Fax: +46(0)300-555 11</p>
  <h2 class="intro-title">Lorem Ipsum</h2>
  <p class="intro-copy">The bulk of the implementation costs will be defined by discovery. Based on similar CRM implementation projects, we feel expect thatlike the CRM side will be somethingfall between 200 and 300 hours, give or take. The wide swing in hours in phase Phase o1ne is related currentlyto the illunder-defined nature of both the integration needs and our role in the integration project. Our focus in discovery Discovery (as mentioned above) will be to nail downfinalize those requirements and our role as it relates to what is needed to integrate the sites with the CRM.</p>
  <div class="cost-table">
    <div class="cell--head">Task</div><div class="cell--head">Hours</div><div class="cell--head">Cost</div>
    <div class="cell cell--task">Discovery</div><div class="cell">40</div><div class="cell">$8,000</div>
    <div class="cell cell--phase">Phase 1</div>
    <div class="cell cell--task">Discovery</div><div class="cell">20-40</div><div class="cell">$8,000</div>
    <div class="cell cell--task">Discovery</div><div class="cell">20-40</div><div class="cell">$8,000</div>
    <div class="cell cell--task">Discovery</div><div class="cell">20-40</div><div class="cell">$8,000</div>
    <div class="cell--total cell--task">Total Phase 1</div><div class="cell--total">80-240</div><div class="cell--total">$16,800-40,000</div>
    <div class="cell cell--phase">Phase 2</div>
    <div class="cell cell--task">Discovery</div><div class="cell">20-40</div><div class="cell">$8,000</div>
    <div class="cell--total cell--task">Total Phase 2</div><div class="cell--total">80-240</div><div class="cell--total">$16,800-40,000</div>
    <div class="cell--grand cell--task">Total Estimated Implementation Cost</div><div class="cell--grand">220-480</div><div class="cell--grand">$44,000-96,000</div>
  </div>
  <h3 class="chart-title">The bulk of the implementation costs will be defined by</h3>
  <p class="chart-copy">The bulk of the implementation costs will be defined by discovery. Based on similar CRM implementation projects, we feel expect thatlike the CRM side will be somethingfall between 200 and 300 hours, give or take. The wide swing in hours in phase Phase o1ne is related currentlyto the illunder-defined nature of both the integration needs and our role in the integration project. Our focus in discovery Discovery (as mentioned above) will be to nail downfinalize</p>
  <svg class="pie-small" role="img" aria-label="Pie chart of cost share by country"><use href="#pie"/></svg>
  <span class="pie-label pie-label--l" style="top:272px">The Netherlands 3.0%</span>
  <span class="pie-label pie-label--l" style="top:277px">Belgium 3.6%</span>
  <span class="pie-label pie-label--l" style="top:282px">UK 6.0%</span>
  <span class="pie-label pie-label--l" style="top:287px">Austria 7.8%</span>
  <span class="pie-label pie-label--l" style="top:292px">Australia 6.5%</span>
  <span class="pie-label pie-label--l" style="top:303px">Germany 10.1%</span>
  <span class="pie-label pie-label--l" style="top:311px">Ireland 12.2%</span>
  <span class="pie-label pie-label--r" style="top:281px">Lithuania 30.5%</span>
  <span class="pie-label pie-label--r" style="top:309px">Czech Republic 18.3%</span>
  <div class="legend">
    <span><i style="background:#80b9e1"></i>Lithuania 30.5%</span><span><i style="background:#6f97d8"></i>Czech Republic 18.3%</span><span><i style="background:#6770c2"></i>Ireland 12.2%</span><span><i style="background:#7a60b6"></i>Germany 10.1%</span>
    <span><i style="background:#9262b7"></i>Australia 6.5%</span><span><i style="background:#ad6cbd"></i>Austria 7.8%</span><span><i style="background:#c676b9"></i>UK 6.0%</span><span><i style="background:#d870a8"></i>Belgium 3.6%</span>
    <span><i style="background:#d9608a"></i>The Netherlands 3.0%</span>
  </div>
  <div class="foot-line"></div>
  <p class="foot-text">Fluxa AB, Granitvägen 12, SE-411 02 Norrvik, SWEDEN &nbsp;| &nbsp;E: info@fluxa-example.com &nbsp;| &nbsp;W: www.fluxa-example.com</p>
</article>

<!-- Sheet 2 -->
<article class="sheet sheet--headline">
  <div class="head-tab"></div>
  <h2 class="head-title">HEADLINE HERE</h2>
  <div class="head-line"></div>
  <h2 class="intro-title">Lorem Ipsum</h2>
  <p class="intro-copy">The bulk of the implementation costs will be defined by discovery. Based on similar CRM implementation projects, we feel expect thatlike the CRM side will be somethingfall between 200 and 300 hours, give or take. The wide swing in hours in phase Phase o1ne is related currentlyto the illunder-defined nature of both the integration needs and our role in the integration project. Our focus in discovery Discovery (as mentioned above) will be to nail downfinalize those requirements and our role as it relates to what is needed to integrate the sites with the CRM.</p>
  <div class="cost-table">
    <div class="cell--head">Task</div><div class="cell--head">Hours</div><div class="cell--head">Cost</div>
    <div class="cell cell--task">Discovery</div><div class="cell">40</div><div class="cell">$8,000</div>
    <div class="cell cell--phase">Phase 1</div>
    <div class="cell cell--task">Discovery</div><div class="cell">20-40</div><div class="cell">$8,000</div>
    <div class="cell cell--task">Discovery</div><div class="cell">20-40</div><div class="cell">$8,000</div>
    <div class="cell cell--task">Discovery</div><div class="cell">20-40</div><div class="cell">$8,000</div>
    <div class="cell--total cell--task">Total Phase 1</div><div class="cell--total">80-240</div><div class="cell--total">$16,800-40,000</div>
    <div class="cell cell--phase">Phase 2</div>
    <div class="cell cell--task">Discovery</div><div class="cell">20-40</div><div class="cell">$8,000</div>
    <div class="cell--total cell--task">Total Phase 2</div><div class="cell--total">80-240</div><div class="cell--total">$16,800-40,000</div>
    <div class="cell--grand cell--task">Total Estimated Implementation Cost</div><div class="cell--grand">220-480</div><div class="cell--grand">$44,000-96,000</div>
  </div>
  <h3 class="chart-title">The bulk of the implementation costs will be defined by</h3>
  <p class="chart-copy">The bulk of the implementation costs will be defined by discovery. Based on similar CRM implementation projects, we feel expect thatlike the CRM side will be somethingfall between 200 and 300 hours, give or take. The wide swing in hours in phase Phase o1ne is related currentlyto the illunder-defined nature of both the integration needs and our role in the integration project. Our focus in discovery Discovery (as mentioned above) will be to nail downfinalize those requirements and</p>
  <svg class="pie-small" role="img" aria-label="Pie chart of cost share by country"><use href="#pie"/></svg>
  <span class="pie-label pie-label--l" style="top:275px">The Netherlands 3.0%</span>
  <span class="pie-label pie-label--l" style="top:280px">Belgium 3.6%</span>
  <span class="pie-label pie-label--l" style="top:285px">UK 6.0%</span>
  <span class="pie-label pie-label--l" style="top:290px">Austria 7.8%</span>
  <span class="pie-label pie-label--l" style="top:295px">Australia 6.5%</span>
  <span class="pie-label pie-label--l" style="top:306px">Germany 10.1%</span>
  <span class="pie-label pie-label--l" style="top:314px">Ireland 12.2%</span>
  <span class="pie-label pie-label--r" style="top:285px">Lithuania 30.5%</span>
  <span class="pie-label pie-label--r" style="top:312px">Czech Republic 18.3%</span>
  <div class="legend">
    <span><i style="background:#80b9e1"></i>Lithuania 30.5%</span><span><i style="background:#6f97d8"></i>Czech Republic 18.3%</span><span><i style="background:#6770c2"></i>Ireland 12.2%</span><span><i style="background:#7a60b6"></i>Germany 10.1%</span>
    <span><i style="background:#9262b7"></i>Australia 6.5%</span><span><i style="background:#ad6cbd"></i>Austria 7.8%</span><span><i style="background:#c676b9"></i>UK 6.0%</span><span><i style="background:#d870a8"></i>Belgium 3.6%</span>
    <span><i style="background:#d9608a"></i>The Netherlands 3.0%</span>
  </div>
  <span class="brand-name foot-brand">Fluxa</span>
  <span class="brand-tag foot-brand-tag">Gas saving for welding</span>
  <div class="foot-rule"></div>
  <p class="foot-contact" style="top:367px">Tel: +46(0)300-555 10 &nbsp;| &nbsp;Fax: +46(0)300-555 11 &nbsp;| &nbsp;E: info@fluxa-example.com &nbsp;| &nbsp;W: www.fluxa-example.com</p>
  <p class="foot-contact" style="top:376px">Fluxa AB, Granitvägen 12, SE-411 02 Norrvik, SWEDEN</p>
</article>

<!-- Sheet 3 -->
<article class="sheet sheet--bar">
  <div class="sheet-brand"><span class="brand-name">Fluxa</span><span class="brand-tag">Gas saving for welding</span></div>
  <div class="head-rule"></div>
  <p class="head-contact">Tel: +46(0)300-555 10 &nbsp;| &nbsp;Fax: +46(0)300-555 11</p>
  <h2 class="intro-title">Lorem Ipsum</h2>
  <p class="intro-copy">The bulk of the implementation costs will be defined by discovery. Based on similar CRM implementation projects, we feel expect thatlike the CRM side will be somethingfall between 200 and 300 hours, give or take. The wide swing in hours in phase Phase o1ne is related currentlyto the illunder-defined nature of both the integration needs and our role in the integration project. Our focus in discovery Discovery (as mentioned above) will be to nail downfinalize those requirements and our role as it relates to what is needed to integrate the sites with the CRM.</p>
  <div class="cost-table">
    <div class="cell--head">Task</div><div class="cell--head">Hours</div><div class="cell--head">Cost</div>
    <div class="cell cell--task">Discovery</div><div class="cell">40</div><div class="cell">$8,000</div>
    <div class="cell cell--phase">Phase 1</div>
    <div class="cell cell--task">Discovery</div><div class="cell">20-40</div><div class="cell">$8,000</div>
    <div class="cell cell--task">Discovery</div><div class="cell">20-40</div><div class="cell">$8,000</div>
    <div class="cell cell--task">Discovery</div><div class="cell">20-40</div><div class="cell">$8,000</div>
    <div class="cell--total cell--task">Total Phase 1</div><div class="cell--total">80-240</div><div class="cell--total">$16,800-40,000</div>
    <div class="cell cell--phase">Phase 2</div>
    <div class="cell cell--task">Discovery</div><div class="cell">20-40</div><div class="cell">$8,000</div>
    <div class="cell--total cell--task">Total Phase 2</div><div class="cell--total">80-240</div><div class="cell--total">$16,800-40,000</div>
    <div class="cell--grand cell--task">Total Estimated Implementation Cost</div><div class="cell--grand">220-480</div><div class="cell--grand">$44,000-96,000</div>
  </div>
  <h3 class="chart-title">The bulk of the implementation costs will be defined by</h3>
  <p class="chart-copy">The bulk of the implementation costs will be defined by discovery. Based on similar CRM implementation projects, we feel expect thatlike the CRM side will be somethingfall between 200 and 300 hours, give or take. The wide swing in hours in phase Phase o1ne is related currentlyto the illunder-defined nature of both the integration needs and our role in the integration project. Our focus in discovery Discovery (as mentioned above) will be to nail downfinalize</p>
  <svg class="pie-small" role="img" aria-label="Pie chart of cost share by country"><use href="#pie"/></svg>
  <span class="pie-label pie-label--l" style="top:272px">The Netherlands 3.0%</span>
  <span class="pie-label pie-label--l" style="top:277px">Belgium 3.6%</span>
  <span class="pie-label pie-label--l" style="top:282px">UK 6.0%</span>
  <span class="pie-label pie-label--l" style="top:287px">Austria 7.8%</span>
  <span class="pie-label pie-label--l" style="top:292px">Australia 6.5%</span>
  <span class="pie-label pie-label--l" style="top:303px">Germany 10.1%</span>
  <span class="pie-label pie-label--l" style="top:311px">Ireland 12.2%</span>
  <span class="pie-label pie-label--r" style="top:281px">Lithuania 30.5%</span>
  <span class="pie-label pie-label--r" style="top:309px">Czech Republic 18.3%</span>
  <div class="legend">
    <span><i style="background:#80b9e1"></i>Lithuania 30.5%</span><span><i style="background:#6f97d8"></i>Czech Republic 18.3%</span><span><i style="background:#6770c2"></i>Ireland 12.2%</span><span><i style="background:#7a60b6"></i>Germany 10.1%</span>
    <span><i style="background:#9262b7"></i>Australia 6.5%</span><span><i style="background:#ad6cbd"></i>Austria 7.8%</span><span><i style="background:#c676b9"></i>UK 6.0%</span><span><i style="background:#d870a8"></i>Belgium 3.6%</span>
    <span><i style="background:#d9608a"></i>The Netherlands 3.0%</span>
  </div>
  <p class="foot-bar">Fluxa AB, Granitvägen 12, SE-411 02 Norrvik, SWEDEN &nbsp;| &nbsp;E: info@fluxa-example.com &nbsp;| &nbsp;W: www.fluxa-example.com</p>
</article>

<h1 class="board-title board-title--slides">Powerpoint template matching with word template</h1>

<!-- Cover slide -->
<section class="slide slide--cover">
  <svg class="slide-shape" viewBox="0 0 486 274" aria-hidden="true">
    <polygon points="0,0 486,0 486,132 0,211" fill="var(--navy)"/>
    <polygon points="0,211 486,132 486,176 0,219" fill="var(--red)"/>
  </svg>
  <h2 class="cover-title">LOREM IPSUM IS SIMPLY<br>DUMMY HAS BEEN</h2>
  <p class="cover-sub">LOREM IPSUM IS SIMPLY ETIAM<br>VESTIBULUM</p>
  <span class="brand-name cover-brand">Fluxa</span>
  <span class="brand-tag cover-tag">Gas saving for welding</span>
</section>

<!-- Contents slide -->
<section class="slide slide--contents">
  <svg class="slide-shape" viewBox="0 0 486 274" aria-hidden="true">
    <polygon points="0,0 219,0 271,86 75,216 0,107" fill="var(--navy)"/>
  </svg>
  <h2 class="contents-title">YOUR <span>OF CONTENTS</span></h2>
  <p class="contents-copy">Tallywise builds automation in stages on top of its current system to reach full automation thanks to the Tallywise AI. Tallywise AI automates every manual task performed by the user. It starts by connecting to all sources of accounting data such as bank accounts, credit card, webshop or document management systems.</p>
  <div class="step-num step-num--1">1</div>
  <div class="step-num step-num--2">2</div>
  <div class="step-num step-num--3">3</div>
  <div class="step step--1"><h4>Tallywise builds automation in stages</h4><p>System to reach full automation thanks to the<br>Tallywise AI. Tallywise AI automates allows.</p></div>
  <div class="step step--2"><h4>Tallywise builds automation in stages</h4><p>System to reach full automation thanks to the<br>Tallywise AI. Tallywise AI automates allows.</p></div>
  <div class="step step--3"><h4>Tallywise builds automation in stages</h4><p>System to reach full automation thanks to the<br>Tallywise AI. Tallywise AI automates allows.</p></div>
  <span class="brand-name slide-brand">Fluxa</span>
  <span class="brand-tag slide-brand-tag">Gas saving for welding</span>
  <div class="slide-rule"></div>
  <div class="page-num">1</div>
</section>

<!-- Content slide -->
<section class="slide slide--content">
  <h2 class="content-title">HEADLINE HERE</h2>
  <div class="content-line"></div>
  <svg class="pie-large" role="img" aria-label="Pie chart of share by country"><use href="#pie"/></svg>
  <div class="legend--large">
    <span><i style="background:#80b9e1"></i>Lithuania 30.5%</span><span><i style="background:#6f97d8"></i>Czech Republic 18.3%</span><span><i style="background:#6770c2"></i>Ireland 12.2%</span><span><i style="background:#7a60b6"></i>Germany 10.1%</span>
    <span><i style="background:#9262b7"></i>Australia 6.5%</span><span><i style="background:#ad6cbd"></i>Austria 7.8%</span><span><i style="background:#c676b9"></i>UK 6.0%</span><span><i style="background:#d870a8"></i>Belgium 3.6%</span>
    <span><i style="background:#d9608a"></i>The Netherlands 3.0%</span>
  </div>
  <div class="content-copy">
    <span>AI automated accounting</span>
    <span>Tallywise builds automation in stages on top of its current system to reach full automation</span>
    <span>thanks to the Tallywise AI. Tallywise AI automates every manual task performed by the user.</span>
    <span>It starts by connecting to all sources of accounting data such as bank accounts, credit card,</span>
    <span>webshop or document management systems (Boxly or Vaultr). Based on these datas,</span>
    <span>Tallywise AI creates bookings and generates financial reports. Finally, Tallywise AI features</span>
    <span>chat-like interface that allows users to communicate seamlessly with it, viewing it as a</span>
    <span>trusted advisor over time for all their accounting queries. software licenses easier for</span>
    <span>software developers. It also makes the management and resale of software license easier for</span>
    <span>software owners. All in all, TaaL has a higher value as a normal . normal software license.</span>
    <span class="copy-sub">Blockchain software license or Token-as-a-License</span>
    <span>It is possible to create tokens on blockchain that represent software licenses, also known as</span>
    <span>Token-as-a-Licence (TaaL). Tallywise creates TaaL by using the Kestrel official wallet which</span>
  </div>
  <span class="brand-name slide-brand">Fluxa</span>
  <span class="brand-tag slide-brand-tag">Gas saving for welding</span>
  <div class="slide-rule" style="width:364px"></div>
  <div class="page-num" style="left:444px">1</div>
</section>

<!-- Closing slide -->
<section class="slide slide--closing">
  <svg class="slide-shape" viewBox="0 0 486 274" aria-hidden="true">
    <polygon points="0,0 486,0 486,132 0,211" fill="var(--navy)"/>
    <polygon points="0,211 486,132 486,176 0,220" fill="var(--red)"/>
  </svg>
  <span class="brand-name closing-brand">Fluxa</span>
  <span class="brand-tag closing-tag">Gas saving for welding</span>
  <div class="closing-sep"></div>
  <p class="closing-info closing-info--a">P: 000-555-0100 Ext 101<br>E: hello@fluxa-example.com<br>W: www.fluxa-example.com</p>
  <p class="closing-info closing-info--b">200, 48 Harbour Lane<br>Sample City, BC 0000</p>
</section>

</body>
</html>
```